Website design for an Italian restaurant in Amsterdam

I need a design for a client of mine. It is for Teatro Lucerna, an Italian restaurant in Amsterdam.
We are going for a clean, modern look but we also need to realise an authentic feel.
The restaurant is located in an old movie theatre, that is where the name Teatro Lucerna comes from.
Industry/Entity Type
Italian Restaurant
Number of Pages Required
1 page
Font styles to use
Sans Serif
Colors
Designer to choose colors to be used in the design.

```html
<!DOCTYPE html>
<html lang="en">
<head>
<meta charset="utf-8">
<title>Teatro Lucerna – Ristorante Italiano</title>
<link rel="stylesheet" href="https://fonts.googleapis.com/css2?family=Roboto:wght@300;400;500;700&family=Cinzel:wght@400;600&family=Great+Vibes&family=Lora:wght@400;700&display=swap">
<style>
:root{
  --white:#ffffff;
  --ink:#3a3a3a;
  --muted:#8c8c8c;
  --rule:#d6d6d6;
  --tan:#ad9471;
  --tan-dark:#9c8363;
  --gold:#e5b629;
  --wine:#b0294a;
  --menu-bg:#f2f1ef;
  --panel:#e4e3e1;
  --field:#c4ae90;
}
*{box-sizing:border-box;margin:0;padding:0}
html,body{width:1200px;height:2423px;overflow:hidden;background:var(--white)}
body{font-family:"Roboto",Arial,sans-serif;color:var(--ink)}
.page{position:relative;width:1200px;height:2423px;overflow:hidden}

/* Header */
.site-header{position:absolute;left:0;top:0;width:1200px;height:92px;background:var(--white);z-index:3}
.nav-link{position:absolute;top:0;height:92px;line-height:113px;font-size:11px;font-weight:500;letter-spacing:.3px;color:#555;text-transform:uppercase}
.nav-link.is-active{background:#ececec;width:66px;text-align:center}
.brand-badge{position:absolute;left:455px;top:0;width:290px;height:118px;z-index:4}
.brand-name{position:absolute;left:0;width:1200px;top:56px;text-align:center;font-family:"Cinzel",Georgia,serif;font-weight:600;font-size:20px;line-height:24px;color:#2b2b2b;z-index:5;letter-spacing:.5px}
.brand-tagline{position:absolute;left:0;width:1200px;top:83px;text-align:center;font-family:"Lora",Georgia,serif;font-size:10px;line-height:12px;color:var(--wine);z-index:5;letter-spacing:.5px}
.brand-dot{position:absolute;left:588px;top:16px;width:24px;height:24px;border-radius:50%;background:var(--wine);z-index:5}

/* Hero */
.hero{position:absolute;left:0;top:92px;width:1200px;height:498px;
  background:radial-gradient(ellipse at 30% 20%,#e8c46a 0%,#9a6d2d 25%,#4a2f17 55%,#2a1a10 100%)}
.hero-panel{position:absolute;left:541px;top:107px;width:384px;height:269px;background:rgba(255,255,255,.18)}
.hero-rule{position:absolute;left:478px;width:244px;height:2px;background:var(--white)}
.hero-welcome{position:absolute;left:0;width:1200px;top:165px;text-align:center;font-family:"Great Vibes",cursive;font-size:72px;line-height:90px;color:var(--white)}
.hero-title{position:absolute;left:0;width:1200px;top:258px;text-align:center;font-family:"Cinzel",Georgia,serif;font-weight:400;font-size:46px;line-height:56px;color:var(--white)}
.hero-sub{position:absolute;left:450px;width:300px;top:327px;text-align:center;font-size:14px;line-height:16px;color:#f1e9dd}

/* Reservation bar */
.reserve-bar{position:absolute;left:0;top:590px;width:1200px;height:74px;background:var(--tan)}
.reserve-heading{position:absolute;left:183px;top:14px;color:var(--white);font-weight:700;font-size:20px;line-height:22px}
.reserve-heading span{display:block;font-weight:300;font-size:14px;line-height:20px}
.reserve-divider{position:absolute;left:318px;top:14px;width:2px;height:46px;background:var(--white)}
.reserve-label{position:absolute;top:26px;font-size:15px;color:var(--white)}
.reserve-field{position:absolute;top:22px;height:34px;background:var(--field);color:#f3ece2;font-size:14px;line-height:34px;padding-left:20px}
.reserve-field svg{position:absolute;right:12px;top:9px}
.reserve-button{position:absolute;left:919px;top:22px;width:98px;height:34px;background:var(--gold);color:var(--white);font-size:13px;font-weight:700;text-align:center;line-height:34px}

/* Section titles */
.section-title{position:absolute;left:0;width:1200px;text-align:center;font-family:"Cinzel",Georgia,serif;font-weight:400;font-size:23px;line-height:28px;color:#555}
.title-rule{position:absolute;left:540px;width:120px;height:1px;background:#bbb}

/* Specials grid */
.specials{position:absolute;left:202px;top:829px;width:796px;height:319px;display:grid;grid-template-columns:repeat(5,1fr);grid-template-rows:repeat(2,1fr)}
.dish-photo{width:100%;height:100%}
.dish-card{background:#f1f1f1;display:flex;flex-direction:column;align-items:center;justify-content:center;padding:0 26px;text-align:center}
.dish-card h3{font-size:14px;font-weight:500;color:#555;letter-spacing:.3px}
.dish-card i{display:block;width:56px;height:1px;background:#c8c8c8;margin:10px 0}
.dish-card p{font-size:9px;line-height:11px;color:#9a9a9a}

/* Menu */
.menu-section{position:absolute;left:0;top:1247px;width:1200px;height:623px;background:linear-gradient(90deg,#efeeec,#f8f8f7 50%,#efeeec)}
.menu-art{position:absolute;left:0;top:0;width:200px;height:417px;background:radial-gradient(circle at 40% 40%,#e3c36a,#8ea34c 45%,#d9d3c6 80%);border-radius:0 0 120px 0}
.menu-tab{position:absolute;top:143px;font-size:14px;line-height:16px;color:#666}
.menu-tab.is-active{left:389px;width:73px;height:28px;top:135px;border:1px solid #999;border-radius:4px;text-align:center;line-height:26px;background:#f8f8f8}
.menu-category{position:absolute;left:310px;font-size:14px;line-height:16px;font-weight:500;color:#555}
.menu-category-band{position:absolute;left:255px;top:256px;width:245px;height:44px;background:#e2e1df}
.menu-panel{position:absolute;left:500px;top:210px;width:442px;height:316px;background:var(--panel);border-radius:4px}
.dish{position:absolute;left:22px;width:400px}
.dish h4{font-size:14px;line-height:17px;font-weight:500;color:#444;margin-bottom:2px}
.dish p{font-size:10px;line-height:15px;color:#8d8d8d;width:300px}
.dish .price{position:absolute;right:0;top:0;font-size:14px;line-height:17px;font-weight:500;color:#444}

/* Testimonials */
.avatar{position:absolute;border-radius:50%}
.avatar-side{width:80px;height:80px;background:radial-gradient(circle,#e8e8e8,#f3f3f3);border:3px solid #f2f2f2}
.avatar-main{left:297px;top:1935px;width:120px;height:120px;background:radial-gradient(circle,#e6dcd4,#cdbfb3);border:4px solid #cdb9a8}
.quote-title{position:absolute;left:446px;top:1954px;font-family:"Lora",Georgia,serif;font-weight:700;font-size:14px;line-height:18px;color:#222}
.quote-body{position:absolute;left:446px;top:1982px;width:490px;font-family:"Lora",Georgia,serif;font-size:10px;line-height:15px;color:#555}
.quote-author{position:absolute;left:648px;top:2030px;font-family:"Lora",Georgia,serif;font-weight:700;font-size:10px;line-height:14px;color:#333}
.rating{position:absolute;left:712px;top:2029px;width:102px;height:15px;background:var(--gold);border-radius:8px;display:flex;align-items:center;padding-left:8px;gap:1px}
.rating small{font-size:7px;color:var(--white);margin-left:6px}
.slider-bar{position:absolute;top:2094px;width:82px;height:4px;background:#d8d8d8}
.slider-bar.is-active{background:var(--gold)}

/* Footer */
.site-footer{position:absolute;left:0;top:2156px;width:1200px;height:239px;background:var(--tan)}
.footer-brand{position:absolute;left:150px;width:272px;top:106px;text-align:center;font-family:"Cinzel",Georgia,serif;font-weight:600;font-size:20px;line-height:24px;color:var(--white)}
.footer-tagline{position:absolute;left:150px;width:272px;top:133px;text-align:center;font-family:"Lora",Georgia,serif;font-size:10px;line-height:12px;color:#f3ece2}
.footer-dot{position:absolute;left:270px;top:62px;width:32px;height:32px;border-radius:50%;border:3px solid var(--white)}
.footer-heading{position:absolute;top:30px;font-size:17px;line-height:20px;font-weight:500;color:var(--white)}
.field{position:absolute;left:480px;width:237px;background:var(--white);border-radius:3px;font-size:11px;line-height:13px;color:#aaa;padding:5px 14px}
.send{position:absolute;left:640px;top:194px;width:77px;height:22px;background:var(--gold);color:var(--white);font-size:11px;font-weight:700;text-align:center;line-height:22px;border-radius:3px}
.address{position:absolute;left:848px;top:66px;font-size:10px;line-height:19px;color:var(--white)}
.social{position:absolute;top:152px;width:16px;height:16px;border-radius:50%;background:var(--white)}
.copyright{position:absolute;left:0;top:2395px;width:1200px;height:28px;background:var(--tan-dark);border-top:1px solid #c7b394;text-align:center;font-size:9px;line-height:28px;color:var(--white)}
</style>
</head>
<body>
<div class="page">

  <header class="site-header">
    <a class="nav-link is-active" style="left:192px">Home</a>
    <a class="nav-link" style="left:280px">Menu</a>
    <a class="nav-link" style="left:350px">Group Menu</a>
    <a class="nav-link" style="left:762px">Reservation</a>
    <a class="nav-link" style="left:873px">Contact</a>
    <a class="nav-link" style="left:961px">Blog</a>
  </header>
  <svg class="brand-badge" viewBox="0 0 290 118" aria-hidden="true">
    <path d="M0 0 H290 V90 Q272 101 252 101 H170 Q152 101 145 113 Q138 101 120 101 H38 Q18 101 0 90 Z" fill="#ffffff"/>
    <path d="M8 98 Q26 108 46 108 H118 Q136 108 145 118 M282 98 Q264 108 244 108 H172 Q154 108 145 118" fill="none" stroke="#ffffff" stroke-width="3"/>
  </svg>
  <span class="brand-dot"></span>
  <div class="brand-name">TEATRO LUCERNA</div>
  <div class="brand-tagline">Ristorante Italiano</div>

  <section class="hero" role="img" aria-label="Warm interior of the restaurant dining room with string lights and set tables">
    <div class="hero-panel"></div>
    <div class="hero-rule" style="top:147px"></div>
    <div class="hero-welcome">Welcome to</div>
    <h1 class="hero-title">TEATRO LUCERNA</h1>
    <p class="hero-sub">The Italian restaurant located in the heart of Amsterdam</p>
    <div class="hero-rule" style="top:389px"></div>
  </section>

  <section class="reserve-bar">
    <div class="reserve-heading">RESERVE<span>YOUR TABLE</span></div>
    <div class="reserve-divider"></div>
    <span class="reserve-label" style="left:347px">Guests</span>
    <div class="reserve-field" style="left:417px;width:171px">no. of guests
      <svg width="20" height="16" viewBox="0 0 20 16"><circle cx="7" cy="5" r="4" fill="#fff"/><path d="M0 16 Q7 6 14 16Z" fill="#fff"/><circle cx="14" cy="5" r="3" fill="#fff"/><path d="M11 10 Q16 7 20 15 H15Z" fill="#fff"/></svg>
    </div>
    <span class="reserve-label" style="left:607px">When</span>
    <div class="reserve-field" style="left:662px;width:231px">select date
      <svg width="16" height="16" viewBox="0 0 16 16"><rect x="1" y="3" width="14" height="12" fill="none" stroke="#fff" stroke-width="2"/><rect x="1" y="3" width="14" height="4" fill="#fff"/><rect x="4" y="0" width="2" height="4" fill="#fff"/><rect x="10" y="0" width="2" height="4" fill="#fff"/></svg>
    </div>
    <div class="reserve-button">RESERVE</div>
  </section>

  <h2 class="section-title" style="top:730px">Monthly Special</h2>
  <div class="title-rule" style="top:774px"></div>

  <section class="specials">
    <div class="dish-photo" role="img" aria-label="Pasta with braised beef and parmesan" style="background:radial-gradient(circle,#c98a3e,#e6c98e 60%,#f3f0ea)"></div>
    <div class="dish-card"><h3>LOREM IPSUM</h3><i></i><p>Lorem ipsum dolor sit amet, consectetur adipiscing elit. Nunc ut.</p></div>
    <div class="dish-photo" role="img" aria-label="Seafood spaghetti with prawns" style="background:radial-gradient(circle,#d9623a,#c9a36a 55%,#3b4a66)"></div>
    <div class="dish-card"><h3>LOREM IPSUM</h3><i></i><p>Lorem ipsum dolor sit amet, consectetur adipiscing elit. Nunc ut.</p></div>
    <div class="dish-photo" role="img" aria-label="Spaghetti with meatballs and basil" style="background:radial-gradient(circle,#9e2a1c,#c9603a 55%,#ece8e2)"></div>
    <div class="dish-card"><h3>LOREM IPSUM</h3><i></i><p>Lorem ipsum dolor sit amet, consectetur adipiscing elit. Nunc ut.</p></div>
    <div class="dish-photo" role="img" aria-label="Seared tuna salad with greens" style="background:radial-gradient(circle,#a8413a,#6e8a3c 50%,#eeeeee)"></div>
    <div class="dish-card"><h3>LOREM IPSUM</h3><i></i><p>Lorem ipsum dolor sit amet, consectetur adipiscing elit. Nunc ut.</p></div>
    <div class="dish-photo" role="img" aria-label="Tagliatelle in tomato sauce" style="background:radial-gradient(circle,#c8522c,#e39a5a 50%,#f2f0ec)"></div>
    <div class="dish-card"><h3>LOREM IPSUM</h3><i></i><p>Lorem ipsum dolor sit amet, consectetur adipiscing elit. Nunc ut.</p></div>
  </section>

  <section class="menu-section">
    <div class="menu-art" role="img" aria-label="Fresh ingredients: tomatoes, dry spaghetti, green pepper and mushrooms"></div>
    <h2 class="section-title" style="top:55px">Menu</h2>
    <div class="title-rule" style="top:92px"></div>
    <div class="menu-tab is-active">Foods</div>
    <div class="menu-tab" style="left:509px">Beverages</div>
    <div class="menu-tab" style="left:638px">Wines</div>
    <div class="menu-tab" style="left:741px">Deserts</div>

    <div class="menu-category-band"></div>
    <div class="menu-category" style="top:226px">Le Insalate</div>
    <div class="menu-category" style="top:269px">Antipasti</div>
    <div class="menu-category" style="top:312px">Le Paste</div>
    <div class="menu-category" style="top:355px">Il Pesce</div>
    <div class="menu-category" style="top:397px">La Carne</div>
    <div class="menu-category" style="top:441px">Contorni</div>
    <div class="menu-category" style="top:483px">Dolce</div>

    <div class="menu-panel">
      <div class="dish" style="top:14px"><h4>Pane Burro e Tapanada</h4><p>Bread, garlicbutter and olivetapenade</p><span class="price">€ 4,50</span></div>
      <div class="dish" style="top:66px"><h4>Carpaccio di Manzo</h4><p>Thinly sliced tenderloin with a pesto of rocketsalad and parmesan cheese</p><span class="price">€ 13,50</span></div>
      <div class="dish" style="top:134px"><h4>Carpaccio di Tonno</h4><p>Thinly sliced tuna with red onion, capers and rocketsalad</p><span class="price">€ 14,50</span></div>
      <div class="dish" style="top:186px"><h4>Vitello Tonnato</h4><p>Thinly sliced veal with Piemonte tunasauce and large capers</p><span class="price">€ 14,75</span></div>
      <div class="dish" style="top:237px"><h4>Antipasto Italiano</h4><p>San Daniële ham, pikante salami, Italiaanse worst, italiaanse kazen, burrata en olijven (min. 2 pers.)</p><span class="price">€ 16,00</span></div>
    </div>
  </section>

  <section class="testimonials">
    <div class="avatar avatar-side" role="img" aria-label="Guest portrait" style="left:97px;top:1955px"></div>
    <div class="avatar avatar-main" role="img" aria-label="Portrait of the reviewing guest"></div>
    <div class="avatar avatar-side" role="img" aria-label="Guest portrait" style="left:1024px;top:1955px"></div>
    <div class="quote-title">Lorem ipsum dolor sit amet, consectetur adipiscing elit.</div>
    <p class="quote-body">Lorem ipsum dolor sit amet, consectetur adipiscing elit. Proin interdum purus quis suscipit viverra. Etiam ullamcorper leo ac auctor aliquet. Vivamus ac dolor malesuada, viverra libero nec, accumsan ligula.</p>
    <div class="quote-author">- Jane Doe</div>
    <div class="rating">
      <svg width="50" height="9" viewBox="0 0 50 9" aria-label="5 stars"><g fill="#ffffff"><path id="s" d="M4.5 0 5.6 3.3 9 3.3 6.3 5.3 7.3 8.6 4.5 6.6 1.7 8.6 2.7 5.3 0 3.3 3.4 3.3Z"/><use href="#s" x="10"/><use href="#s" x="20"/><use href="#s" x="30"/><use href="#s" x="40"/></g></svg>
      <small>5 stars</small>
    </div>
    <div class="slider-bar" style="left:472px"></div>
    <div class="slider-bar is-active" style="left:557px"></div>
    <div class="slider-bar" style="left:643px"></div>
  </section>

  <footer class="site-footer">
    <span class="footer-dot"></span>
    <div class="footer-brand">TEATRO LUCERNA</div>
    <div class="footer-tagline">Ristorante Italiano</div>

    <h3 class="footer-heading" style="left:480px">Contact Us</h3>
    <div class="field" style="top:63px;height:23px">Your name</div>
    <div class="field" style="top:90px;height:23px">Email</div>
    <div class="field" style="top:118px;height:66px">Message</div>
    <div class="send">SEND</div>

    <h3 class="footer-heading" style="left:848px">Address</h3>
    <div class="address">Teatro Lucerna<br>Lindengracht 42<br>1015 KB Amsterdam<br>Tel nr.: (+31) 20 555 0142</div>
    <span class="social" style="left:851px"></span>
    <span class="social" style="left:884px"></span>
    <span class="social" style="left:918px"></span>
  </footer>
  <div class="copyright">Copyright teatrolucerna.example. All Right Reserved.</div>

</div>
</body>
</html>
```